Brookvale Insurance Services - Insurance Agency Wesbite

I need a website for my insurance agency called Brookvale Insurance Services. I have attached my company logo. You can use the colors from the copy logo to create the website color scheme. I need a Request A Quote section.
Business Address: 7816 Marlowe Ave Unit D, Studio City Ca 91627
Business Phone: (818) 555-0193
I would need the following drop downs on the main page:

1st drop down:
Business Insurance
⁃ Commercial Auto
⁃ Employment Practice Liability Insurance
⁃ General Liability Insurance
⁃ Professional Liability Insurance
⁃ Property Insurance
⁃ Workers Compensation Insurance

2nd drop down:
Industries We Serve
- Construction
- Janitorial
- Landscapers
- Trucking
- ParcelRun Independent Service Providers (ISP)
Healthcare Industry
- Community Care Facilities
- Home Health Agencies
- Hospice
- Nursing Homes

3rd drop down:
Risk Management
- Claims Management
- Compliance & Risk Management

4th drop down
Request a quote

5th drop down
About Us

6th drop down
Contact US

Target Market(s)

Potential clients

Industry/Entity Type

Business Insurance

Coding

Coded - Design and coding required

Number of Pages Required

5+ page

Colors
0054AA
0677BA
7BADD7
CADEEF
E8F1F8
00AB8E
00BBA5
67D7C9
C6EFE9
E9F9F6

Requirements
Must have
• Home Business Insurance - Commercial Auto - Employment Practice Liability Insurance - General Liability Insurance - Professional Liability Insurance - Property Insurance - Workers Compensation Insurance Industries We Serve - Construction - Janitorial - Landscapers - Manufacturing Companies - Restaurants - Towing - Trucking Healthcare Industry - Community Care Facilities - Home Health Agencies - Hospice - Nursing Homes - Risk Management - Claims Management - Compliance & Risk Management Request a Quote About Us Contact Us

```html
<!DOCTYPE html>
<html lang="en">
<head>
<meta charset="utf-8">
<title>Brookvale Insurance Services</title>
<link href="https://fonts.googleapis.com/css2?family=Roboto:wght@400;500;700&family=Pinyon+Script&display=swap" rel="stylesheet">
<style>
:root{
  --navy:#0b2c8f;
  --navy-dark:#0a2680;
  --green:#1f9a3a;
  --text:#222a33;
  --muted:#4a4f58;
  --band:#e4edfb;
  --field:#eeeff1;
  --white:#ffffff;
}
*{box-sizing:border-box;margin:0;padding:0}
html,body{width:1200px;height:4422px;overflow:hidden}
body{position:relative;font-family:'Roboto',sans-serif;color:var(--text);background:var(--white)}
.abs{position:absolute}
.nav{top:0;left:0;width:1200px;height:69px;background:var(--white)}
.brand{color:var(--navy);font-weight:700;line-height:1}
.brand .name{font-size:27px;letter-spacing:.5px}
.brand .sub{font-size:10px;letter-spacing:3px;margin-top:4px}
.nav-links{top:26px;left:306px;display:flex;gap:0;font-size:12px;color:#333}
.nav-links span{position:absolute;white-space:nowrap}
.nav-links .active{color:var(--green)}
.btn{background:var(--navy);color:var(--white);display:flex;align-items:center;justify-content:center;font-size:15px;font-weight:500}
.hero{top:69px;left:0;width:1200px;height:606px;background:linear-gradient(120deg,#c9c9c9,#e6e6e6 45%,#b4b4b4)}
.welcome{top:248px;left:110px;font-family:'Pinyon Script',cursive;font-size:38px;color:#1f2a55}
.hero-title{top:306px;left:110px;font-size:37px;font-weight:700;color:var(--green);line-height:45px}
.hero-text{top:406px;left:110px;width:460px;font-size:11px;line-height:22px;color:#222}
.section-title{left:0;width:1200px;text-align:center;font-size:36px;font-weight:700}
.section-title .g{color:var(--green)}.section-title .n{color:var(--navy)}
.rule{left:550px;width:110px;height:4px;background:linear-gradient(90deg,var(--navy) 50%,var(--green) 50%)}
.photo{background:linear-gradient(135deg,#8a6a5a,#c8b6a6 50%,#5d5a60)}
.cover-item{left:650px;display:flex;align-items:center;font-size:13px;font-weight:700;color:#1a1f2a}
.cover-item .ico{width:40px;height:40px;border-radius:50%;background:var(--white);box-shadow:0 0 8px rgba(0,0,0,.12);display:flex;align-items:center;justify-content:center;margin-right:16px}
.band{top:1399px;left:0;width:1200px;height:778px;background:var(--band)}
.card-title{font-size:22px;font-weight:500;color:#1b1f27}
.card-text{font-size:11px;line-height:18.5px;color:#333;width:465px}
.list-head{font-size:16px;font-weight:700;color:#222;left:752px}
.list{left:752px;font-size:14px;color:#333;line-height:29.3px;list-style:none}
.list li::before{content:"✓";color:var(--navy);font-weight:700;margin-right:8px}
.map{top:2812px;left:0;width:1200px;height:656px;background:linear-gradient(90deg,#eceff3,#e3e8ee 60%,#d6e6f3)}
.quote{top:2876px;left:120px;width:632px;height:524px;background:var(--white)}
.quote h2{position:absolute;top:32px;left:32px;font-size:35px;font-weight:700;color:var(--green)}
.field{background:var(--field);font-size:10px;color:#555;padding:16px 17px}
.event{background:var(--navy);color:var(--white);width:285px;height:316px}
.event .img{position:absolute;top:6px;left:6px;width:273px;height:178px;background:linear-gradient(135deg,#6f7e92,#c9c4bb 55%,#4f5a68)}
.event h3{position:absolute;top:202px;left:11px;width:265px;font-size:17px;font-weight:500;line-height:22px}
.event .date{position:absolute;top:246px;left:11px;font-size:10px;font-weight:700}
.event p{position:absolute;top:264px;left:11px;width:235px;font-size:10px;font-weight:500;line-height:15px}
.arrow{width:44px;height:44px;border-radius:50%;border:1.5px solid #333;display:flex;align-items:center;justify-content:center;top:3728px}
.partner{top:4005px;font-size:24px;font-weight:700;color:#8a8f98;transform:translateX(-50%);white-space:nowrap}
.footer{top:4103px;left:0;width:1200px;height:319px;background:var(--navy-dark);color:var(--white)}
.fhead{font-size:13px;color:var(--green);font-weight:500}
.fitem{font-size:11px;color:var(--white);display:flex;align-items:center;gap:8px}
.dot{width:14px;height:14px;border-radius:50%;background:var(--green);display:inline-block}
</style>
</head>
<body>

<header class="abs nav">
  <div class="abs brand" style="top:16px;left:120px"><div class="name">BROOKVALE</div><div class="sub">INSURANCE SERVICES</div></div>
  <nav class="abs nav-links" style="left:0">
    <span class="active" style="left:306px">Home</span>
    <span style="left:386px">About Us</span>
    <span style="left:481px">Business Insurance ⌄</span>
    <span style="left:635px">Industries We Serve ⌄</span>
    <span style="left:790px">Risk Management ⌄</span>
  </nav>
  <div class="abs btn" style="top:9px;left:934px;width:144px;height:49px;font-size:14px">Contact us</div>
</header>

<section class="abs hero" role="img" aria-label="Photo of an older couple smiling while reviewing insurance papers at a laptop"></section>
<div class="abs welcome">Welcome to</div>
<h1 class="abs hero-title">BROOKVALE INSURANCE<br>SERVICES</h1>
<p class="abs hero-text">Lorem Ipsum is simply dummy text of the printing and typesetting industry. Lorem Ipsum has been the industry's standard dummy text ever since the 1500s, when an unknown printer took a galley of type and scrambled it to make a type specimen book.</p>
<div class="abs btn" style="top:491px;left:112px;width:156px;height:52px;font-size:17px">Get started</div>

<h2 class="abs section-title" style="top:734px"><span class="g">BUSINESS</span> <span class="n">INSURANCE</span></h2>
<div class="abs rule" style="top:784px"></div>
<div class="abs photo" style="top:915px;left:112px;width:559px;height:419px" role="img" aria-label="Photo of two advisers reviewing a document on a clipboard"></div>
<div class="abs cover-item" style="top:947px"><span class="ico"><svg width="20" height="14" viewBox="0 0 20 14" fill="none" stroke="#0b2c8f" stroke-width="1.3"><rect x="1" y="3" width="12" height="7"/><path d="M13 5h4l2 3v2h-6"/><circle cx="5" cy="11.5" r="1.5"/><circle cx="15" cy="11.5" r="1.5"/></svg></span>Commercial Auto</div>
<div class="abs cover-item" style="top:1012px"><span class="ico"><svg width="18" height="18" viewBox="0 0 18 18" fill="none" stroke="#0b2c8f" stroke-width="1.3"><circle cx="9" cy="6" r="3"/><path d="M3 16c0-4 3-6 6-6s6 2 6 6"/></svg></span>Employment Practice Liability Insurance</div>
<div class="abs cover-item" style="top:1074px"><span class="ico"><svg width="18" height="18" viewBox="0 0 18 18" fill="none" stroke="#0b2c8f" stroke-width="1.3"><circle cx="7" cy="5" r="3"/><path d="M1 16c0-4 3-6 6-6"/><path d="M11 11l2 2 4-4"/></svg></span>General Liability Insurance</div>
<div class="abs cover-item" style="top:1135px"><span class="ico"><svg width="18" height="18" viewBox="0 0 18 18" fill="none" stroke="#0b2c8f" stroke-width="1.3"><circle cx="9" cy="4" r="2.5"/><path d="M5 17V10h8v7M9 10v7"/></svg></span>Professional Liability Insurance</div>
<div class="abs cover-item" style="top:1204px"><span class="ico"><svg width="20" height="18" viewBox="0 0 20 18" fill="none" stroke="#0b2c8f" stroke-width="1.3"><path d="M2 9l8-7 8 7M4 8v8h12V8"/><rect x="8" y="11" width="4" height="5"/></svg></span>Property Insurance</div>
<div class="abs cover-item" style="top:1266px"><span class="ico"><svg width="18" height="18" viewBox="0 0 18 18" fill="none" stroke="#0b2c8f" stroke-width="1.3"><path d="M9 1l7 3v5c0 4-3 7-7 8-4-1-7-4-7-8V4z"/><path d="M6 9l2 2 4-4"/></svg></span>Workers Compensation Insurance</div>

<section class="abs band"></section>
<h2 class="abs section-title" style="top:1458px"><span class="g">RISK</span> <span class="n">MANAGEMENT</span></h2>
<div class="abs rule" style="top:1511px;left:527px;width:140px"></div>
<div class="abs photo" style="top:1573px;left:122px;width:467px;height:291px;background:linear-gradient(135deg,#7b6a55,#d9d3c8 50%,#3d4150)" role="img" aria-label="Photo of an adviser handing documents to a client across an office desk"></div>
<div class="abs photo" style="top:1571px;left:610px;width:468px;height:293px;background:linear-gradient(135deg,#6d5f4f,#d6d0c4 50%,#2f3440)" role="img" aria-label="Photo of two colleagues discussing compliance papers at an office desk"></div>
<div class="abs card-title" style="top:1873px;left:122px">Claims Management</div>
<p class="abs card-text" style="top:1906px;left:122px">Our approach to claims management involves close collaboration with clients. We ensure they grasp the process and receive the necessary support for effective claim filing and management. From guiding on required documentation to advocating for fair and prompt handling, we are dedicated to assisting clients throughout the claims process.</p>
<div class="abs btn" style="top:2000px;left:122px;width:132px;height:50px;font-size:14px">Learn More</div>
<div class="abs card-title" style="top:1873px;left:610px">Compliance &amp; Risk Management</div>
<p class="abs card-text" style="top:1906px;left:610px">Effective risk management is crucial in today's landscape, where auto insurance rates are soaring, EPLI claims are on the rise, and businesses face escalating liabilities. Whether in trucking or construction, the inherent risks of job sites or road presence demand careful consideration. From injuries on construction sites to vehicle breakdowns, potential accidents are numerous.</p>
<div class="abs btn" style="top:2014px;left:611px;width:132px;height:50px;font-size:14px">Learn More</div>

<div class="abs photo" style="top:2249px;left:122px;width:556px;height:486px;background:linear-gradient(135deg,#a89a8a,#e2d8cc 50%,#6a6f60)" role="img" aria-label="Photo of a smiling man and woman working together at a desk"></div>
<div class="abs list-head" style="top:2313px">INDUSTRIES WE SERVE</div>
<ul class="abs list" style="top:2338px"><li>Construction</li><li>Janitorial</li><li>Landscapers</li><li>Manufacturing Companies</li><li>Restaurants</li><li>Towing</li><li>Trucking</li></ul>
<div class="abs list-head" style="top:2572px">HEALTHCARE INDUSTRY</div>
<ul class="abs list" style="top:2594px"><li>Community Care Facilities</li><li>Home Health Agencies</li><li>Hospice</li><li>Nursing Homes</li></ul>

<section class="abs map" role="img" aria-label="Street map showing the office location"></section>
<svg class="abs" style="top:3150px;left:890px" width="26" height="36" viewBox="0 0 26 36"><path d="M13 35C13 35 25 20 25 12A12 12 0 0 0 1 12c0 8 12 23 12 23z" fill="#e53935"/><circle cx="13" cy="12" r="4" fill="#8b1a1a"/></svg>
<form class="abs quote">
  <h2>REQUEST A QUOTE</h2>
  <div class="abs field" style="top:91px;left:33px;width:276px;height:48px">First Name:</div>
  <div class="abs field" style="top:91px;left:328px;width:277px;height:48px">Last Name:</div>
  <div class="abs field" style="top:159px;left:33px;width:572px;height:48px">Email:</div>
  <div class="abs field" style="top:228px;left:33px;width:572px;height:48px">Address:</div>
  <div class="abs field" style="top:297px;left:33px;width:572px;height:93px">Message:</div>
  <div class="abs btn" style="top:415px;left:33px;width:132px;height:52px;font-size:14px">Submit</div>
</form>

<h2 class="abs section-title" style="top:3526px"><span class="g">LATEST EVENTS</span></h2>
<div class="abs rule" style="top:3580px;left:543px"></div>
<div class="abs arrow" style="left:45px"><svg width="10" height="16" viewBox="0 0 10 16" fill="none" stroke="#333" stroke-width="1.6"><path d="M8 1L2 8l6 7"/></svg></div>
<div class="abs arrow" style="left:1104px"><svg width="10" height="16" viewBox="0 0 10 16" fill="none" stroke="#333" stroke-width="1.6"><path d="M2 1l6 7-6 7"/></svg></div>
<article class="abs event" style="top:3602px;left:156px"><div class="img" role="img" aria-label="Photo of an adviser meeting a client"></div><h3>Lorem Ipsum is simply dummy text of the printing and</h3><div class="date">April 15 – April 20, 2023</div><p>Lorem Ipsum is simply dummy text of the printing and typesetting industry.</p></article>
<article class="abs event" style="top:3602px;left:455px"><div class="img" role="img" aria-label="Photo of two colleagues talking in an office"></div><h3>Lorem Ipsum is simply dummy text of the printing and</h3><div class="date">April 15 – April 20, 2023</div><p>Lorem Ipsum is simply dummy text of the printing and typesetting industry.</p></article>
<article class="abs event" style="top:3602px;left:754px"><div class="img" role="img" aria-label="Photo of a couple reviewing plans with an adviser"></div><h3>Lorem Ipsum is simply dummy text of the printing and</h3><div class="date">April 15 – April 20, 2023</div><p>Lorem Ipsum is simply dummy text of the printing and typesetting industry.</p></article>

<div class="abs partner" style="left:158px;font-size:11px;top:4014px;text-align:center;font-weight:500">■<br>COMPANY NAME</div>
<div class="abs partner" style="left:343px">northpeak</div>
<div class="abs partner" style="left:553px">FIELDLINE</div>
<div class="abs partner" style="left:781px">tidewell</div>
<div class="abs partner" style="left:996px">VANTARO</div>

<footer class="abs footer">
  <div class="abs brand" style="top:64px;left:122px;color:var(--white)"><div class="name">BROOKVALE</div><div class="sub">INSURANCE SERVICES</div></div>
  <p class="abs" style="top:121px;left:122px;width:180px;font-size:9px;line-height:15px">Lorem Ipsum is simply dummy text of the printing and typesetting industry. Lorem Ipsum has been the industry's standard dummy text</p>
  <div class="abs fhead" style="top:62px;left:374px">MENU</div>
  <div class="abs fitem" style="top:85px;left:374px">Home</div>
  <div class="abs fitem" style="top:115px;left:374px">About Us</div>
  <div class="abs fitem" style="top:145px;left:374px">Business Insurance</div>
  <div class="abs fitem" style="top:175px;left:374px">Industries We Serve</div>
  <div class="abs fitem" style="top:204px;left:374px">Risk Management</div>
  <div class="abs fhead" style="top:62px;left:570px">CONTACT US</div>
  <div class="abs fitem" style="top:86px;left:570px"><span class="dot"></span>(818) 555-0193</div>
  <div class="abs fitem" style="top:114px;left:570px"><span class="dot"></span>7816 Marlowe Ave Unit D, Studio City Ca 91627</div>
  <div class="abs fitem" style="top:140px;left:570px"><span class="dot"></span>info@brookvaleinsurance.com</div>
  <div class="abs fhead" style="top:65px;left:934px">FOLLOW US</div>
  <div class="abs fitem" style="top:90px;left:934px"><span class="dot"></span>Circlebook</div>
  <div class="abs fitem" style="top:116px;left:934px"><span class="dot"></span>Streamly</div>
  <div class="abs fitem" style="top:141px;left:934px"><span class="dot"></span>Snapgrid</div>
  <div class="abs fitem" style="top:167px;left:934px"><span class="dot"></span>Chirpline</div>
  <div class="abs" style="top:261px;left:0;width:1200px;height:1px;background:rgba(255,255,255,.25)"></div>
  <div class="abs" style="top:284px;left:0;width:1200px;text-align:center;font-size:9px">Copyright © 2010-2024 Brookvale Insurance Services S.L. All rights reserved.</div>
</footer>

</body>
</html>
```